Wendy Marsh Copywriter Website

I am starting a new business as a freelance copywriter. Trying to set up the website for my business is proving to be too technical for me. I would like a simple, clean website using primarily black and white. I have attached the logo I would like used. I would like the menu icons to be Home, Services, Portfolio, Blog, Contact. I would like my mobile phone number (0412 583 906) and email address (wendy.marsh.copywriter@mailbox-example.com) used in the header of the site. I need the site to be easily manageable and inter-changeable for me to be able to move things around and add images, etc with ease.

I would like the home page to be a static page with space for an image of myself somewhere (I haven't had this taken as yet), an area to put a bit about myself and my business, and also somewhere to include social media icons/links. Again, I would like the whole website and home page to be easily managed so that I can add/delete things with ease.

I would like the image of the typewriter used in the website somewhere also please.

Font styles to use
Sans Serif
Script

Colors
fdf0f6

Requirements
Must have
• The logo provided
• Ability to change page contents easily
• Ability to add social media icons as needed
Nice to have
• Use of the typewriter image
Should not have
• Complicated pages that are not easily editable

```html
<!DOCTYPE html>
<html lang="en">
<head>
<meta charset="utf-8">
<title>Wendy Marsh Copywriter</title>
<link rel="stylesheet" href="https://fonts.googleapis.com/css2?family=Dancing+Script:wght@600;700&family=Open+Sans:wght@400;600&family=Poppins:wght@400;500&display=swap">
<style>
:root{
  --ink:#1c1c1c;
  --text:#555555;
  --blush:#fdf0f6;
  --blush-deep:#f2dde4;
  --rose:#f7dfe7;
  --rose-line:#e2b9c8;
  --white:#ffffff;
  --night:#0d0d0d;
  --night-2:#141414;
  --slate:#4a4a4a;
  --script:'Dancing Script', cursive;
  --sans:'Poppins', sans-serif;
  --body:'Open Sans', sans-serif;
}
*{margin:0;padding:0;box-sizing:border-box}
html,body{width:1200px;height:3220px;overflow:hidden}
body{position:relative;background:var(--white);font-family:var(--body);color:var(--text)}
.abs{position:absolute}
a{color:inherit;text-decoration:none}

/* header */
.site-header{position:absolute;left:0;top:0;width:1200px;height:120px;background:var(--white)}
.brand{left:88px;top:24px;font-family:var(--sans);font-weight:400;font-size:30px;color:var(--ink);letter-spacing:.5px;display:flex;align-items:center;gap:12px}
.brand-mark{width:14px;height:14px;background:var(--rose-line)}
.header-contact{right:88px;top:30px;display:flex;gap:26px;font-family:var(--sans);font-size:13.5px;color:var(--ink)}
.header-contact span{display:flex;align-items:center;gap:7px}
.main-nav{right:88px;top:66px;display:flex;gap:50px;font-family:var(--sans);font-size:17px;color:var(--ink)}

/* hero */
.hero{left:0;top:120px;width:1200px;height:556px}
.hero-photo{position:absolute;inset:0;background:linear-gradient(100deg,#d9d6d8 0%,#c8c2c4 30%,#9c9598 55%,#6f6a6c 100%)}
.hero-badge{left:554px;top:159px;width:700px;height:219px;border-radius:110px 0 0 110px;background:rgba(60,58,60,.82);border:5px solid var(--rose-line);border-right:none;color:var(--white);text-align:center;padding-right:100px}
.hero-badge h1{font-family:var(--script);font-weight:700;font-size:84px;line-height:1;margin-top:20px}
.hero-badge p{font-family:var(--script);font-weight:600;font-size:44px;line-height:1.2}

/* about */
.about{left:0;top:676px;width:1200px;height:458px;background:linear-gradient(90deg,#fff 55%,#f4f3f4 75%,#ececec 100%)}
.about-photo{right:0;top:0;width:367px;height:458px;background:linear-gradient(180deg,#dcdad9,#b8b0ad 60%,#8a8285)}
.script-title{font-family:var(--script);font-weight:700;color:var(--ink);font-size:40px;line-height:1}
.copy{font-size:14.3px;line-height:28.5px;color:var(--text);text-align:justify}
.btn{display:inline-block;font-family:var(--sans);font-size:16px;color:var(--ink);background:var(--rose);border:2px solid var(--rose-line);border-radius:18px;text-align:center;line-height:30px;height:36px}

/* services */
.services{left:0;top:1134px;width:1200px;height:573px;background:linear-gradient(160deg,#f6e5ea,#efdbe1 50%,#f3e2e7)}
.section-title{left:0;width:1200px;text-align:center}
.service-card{width:312px;height:247px;top:1342px;background:var(--white);border:1px solid #d8cfd2;text-align:center}
.service-icon{position:absolute;left:103px;top:-56px;width:107px;height:107px;border-radius:50%;background:var(--white);box-shadow:0 2px 8px rgba(0,0,0,.12);display:flex;align-items:center;justify-content:center}
.service-card h3{font-family:var(--sans);font-weight:400;font-size:20px;color:var(--ink);margin-top:80px}
.service-card p{font-size:14px;line-height:25px;margin:14px auto 0;width:240px}
.service-card .btn{position:absolute;left:98px;bottom:-17px;width:116px;height:33px;line-height:29px;font-size:14px;background:var(--white);border:1.5px solid #777}
.service-card .btn.is-active{background:var(--rose);border-color:var(--rose-line)}

/* work */
.work-frame{left:88px;top:1818px;width:412px;height:314px;border:3px solid var(--ink)}
.work-photo{left:116px;top:1840px;width:401px;height:316px;background:radial-gradient(ellipse at 48% 55%,#3a3a3a 0%,#5e5e5e 28%,#d9d9d9 48%,#ececec 100%);box-shadow:0 6px 14px rgba(0,0,0,.25)}

/* blog */
.blog{left:0;top:2270px;width:1200px;height:560px;background:linear-gradient(160deg,#f6e5ea,#f0dde3 55%,#f4e4e9)}
.post{width:312px;top:2441px}
.post-photo{width:312px;height:174px}
.post-meta{display:flex;margin-top:13px;height:20px;font-size:12px;line-height:20px;color:var(--white)}
.post-date{width:69px;background:#6c6c6c;text-align:center}
.post-comments{width:34px;background:#222;display:flex;align-items:center;justify-content:center;gap:3px}
.post h3{font-family:var(--body);font-weight:400;font-size:16px;color:var(--ink);margin-top:12px}
.post p{font-size:12.3px;line-height:21px;margin-top:4px}
.post .more{font-size:12.3px;color:var(--ink);margin-top:8px;display:block}

/* footer */
.footer-rule{left:0;top:2830px;width:1200px;height:10px;background:var(--slate)}
.site-footer{left:0;top:2840px;width:1200px;height:306px;background:var(--night);color:var(--white)}
.footer-col{top:78px}
.footer-col h4{font-family:var(--body);font-weight:400;font-size:18px;letter-spacing:.3px}
.footer-col ul{list-style:none;margin-top:18px}
.footer-col li{font-size:14.5px;line-height:33px}
.contact-item{display:flex;gap:12px;margin-top:18px}
.contact-item b{display:block;font-weight:600;font-size:14.5px}
.contact-item span{font-size:14px}
.socials{display:flex;gap:12px;margin-top:22px}
.socials span{width:26px;height:26px;background:var(--white);border-radius:3px}
.footer-bottom{left:0;top:3146px;width:1200px;height:74px;background:var(--night-2);color:#9a9a9a;text-align:center;font-size:13.5px;line-height:74px}
</style>
</head>
<body>

<header class="site-header">
  <div class="abs brand"><span class="brand-mark"></span>Wendy Marsh Copywriter</div>
  <div class="abs header-contact">
    <span><svg width="12" height="12" viewBox="0 0 24 24"><path d="M6.6 10.8a15 15 0 006.6 6.6l2.2-2.2a1 1 0 011-.25 11.4 11.4 0 003.6.6 1 1 0 011 1V20a1 1 0 01-1 1A17 17 0 013 4a1 1 0 011-1h3.5a1 1 0 011 1c0 1.25.2 2.45.57 3.57a1 1 0 01-.25 1z" fill="#1c1c1c"/></svg>0412 583 906</span>
    <span><svg width="13" height="10" viewBox="0 0 26 20"><rect x="1" y="1" width="24" height="18" fill="none" stroke="#1c1c1c" stroke-width="2"/><path d="M1 1l12 10L25 1" fill="none" stroke="#1c1c1c" stroke-width="2"/></svg>wendy.marsh.copywriter@mailbox-example.com</span>
  </div>
  <nav class="abs main-nav"><a>Home</a><a>Services</a><a>Portfolio</a><a>Blog</a><a>Contact</a></nav>
</header>

<section class="abs hero">
  <div class="hero-photo" role="img" aria-label="Photo of a copywriter writing notes at a desk beside a laptop"></div>
  <div class="abs hero-badge">
    <h1>Wendy Marsh</h1>
    <p>I'm a freelance copywriter</p>
  </div>
</section>

<section class="abs about">
  <h2 class="abs script-title" style="left:152px;top:92px">About me</h2>
  <p class="abs copy" style="left:152px;top:148px;width:535px">It is a long established fact that a reader will be distracted by the readable content of a page when looking at its layout. The point of using Lorem Ipsum is that it has a more-or-less normal distribution of letters, as opposed to using 'Content here, content here', making it look like readable English. Many desk-top publishing packages and web page editors now use Lorem Ipsum as their default model text, and a search for 'lorem ipsum' will uncover many</p>
  <a class="abs btn" style="left:152px;top:330px;width:124px">Read More</a>
  <div class="abs about-photo" role="img" aria-label="Portrait photo of the copywriter"></div>
</section>

<section class="abs services">
  <h2 class="abs section-title script-title" style="top:76px">Our Services</h2>
</section>

<article class="abs service-card" style="left:105px">
  <div class="service-icon"><svg width="46" height="46" viewBox="0 0 46 46" fill="none" stroke="#1c1c1c" stroke-width="2.5"><path d="M10 4h20l6 6v30H10z"/><path d="M16 14h14M16 20h14M16 26h8"/><path d="M38 24l-10 12-4 1 1-4 10-12z"/></svg></div>
  <h3>Porro quisquam</h3>
  <p>It is a long established fact that a reader will be distracted by the readable content of a page</p>
  <a class="btn">Read more</a>
</article>
<article class="abs service-card" style="left:447px">
  <div class="service-icon"><svg width="48" height="46" viewBox="0 0 48 46" fill="none" stroke="#1c1c1c" stroke-width="2.5"><path d="M14 4h20v12H14z"/><rect x="4" y="16" width="40" height="22" rx="2"/><path d="M10 24h28M10 30h28M14 42h20"/></svg></div>
  <h3>Dolorem ipsum quia</h3>
  <p>It is a long established fact that a reader will be distracted by the readable content of a page</p>
  <a class="btn is-active">Read more</a>
</article>
<article class="abs service-card" style="left:790px">
  <div class="service-icon"><svg width="46" height="46" viewBox="0 0 46 46" fill="none" stroke="#1c1c1c" stroke-width="2.5"><circle cx="17" cy="11" r="6"/><path d="M6 30c0-7 5-11 11-11"/><path d="M22 22h14l4 4v16H22z"/><path d="M26 30h10M26 36h10"/></svg></div>
  <h3>Neque porro quisquam</h3>
  <p>It is a long established fact that a reader will be distracted by the readable content of a page</p>
  <a class="btn">Read more</a>
</article>

<section class="abs" style="left:0;top:1707px;width:1200px;height:563px">
  <h2 class="abs script-title" style="left:593px;top:146px">My Work</h2>
  <p class="abs copy" style="left:580px;top:218px;width:532px">It is a long established fact that a reader will be distracted by the readable content of a page when looking at its layout. The point of using Lorem Ipsum is that it has a more-or-less normal distribution of letters, as opposed to using 'Content here, content here', making it look like readable English. Many desk-top publishing packages and web page editors now use Lorem Ipsum as their default model text, and a search for 'lorem ipsum' will uncover many</p>
  <a class="abs btn" style="left:580px;top:401px;width:124px">Read More</a>
</section>
<div class="abs work-frame"></div>
<div class="abs work-photo" role="img" aria-label="Photo of a black vintage typewriter with a sheet of paper"></div>

<section class="abs blog">
  <h2 class="abs section-title script-title" style="top:78px">Latest Blog</h2>
</section>

<article class="abs post" style="left:94px">
  <div class="post-photo" role="img" aria-label="Photo of a person working on a laptop by a window" style="background:linear-gradient(135deg,#2d3440,#6b7a88 50%,#1f2329)"></div>
  <div class="post-meta"><span class="post-date">Dec 03</span><span class="post-comments"><svg width="11" height="9" viewBox="0 0 11 9"><path d="M1 1h9v5H4l-2 2V6H1z" fill="none" stroke="#fff"/></svg>0</span></div>
  <h3>Neque porro quisquam dolorem</h3>
  <p>It has survived not only five centuries, but also the leap into electronic typesetting,</p>
  <a class="more">Read More »</a>
</article>
<article class="abs post" style="left:442px">
  <div class="post-photo" role="img" aria-label="Photo of a woman writing at a table with a laptop" style="background:linear-gradient(135deg,#3a3a3c,#c9b9a8 50%,#8a7f78)"></div>
  <div class="post-meta"><span class="post-date">Dec 03</span><span class="post-comments"><svg width="11" height="9" viewBox="0 0 11 9"><path d="M1 1h9v5H4l-2 2V6H1z" fill="none" stroke="#fff"/></svg>0</span></div>
  <h3>Porro quisquam est qui</h3>
  <p>It has survived not only five centuries, but also the leap into electronic typesetting,</p>
  <a class="more">Read More »</a>
</article>
<article class="abs post" style="left:797px">
  <div class="post-photo" role="img" aria-label="Photo of hands typing on a typewriter, seen from above" style="background:linear-gradient(135deg,#2a2623,#6d645c 50%,#d6d2cd)"></div>
  <div class="post-meta"><span class="post-date">Dec 03</span><span class="post-comments"><svg width="11" height="9" viewBox="0 0 11 9"><path d="M1 1h9v5H4l-2 2V6H1z" fill="none" stroke="#fff"/></svg>0</span></div>
  <h3>Dolorem ipsum quia dolor</h3>
  <p>It has survived not only five centuries, but also the leap into electronic typesetting,</p>
  <a class="more">Read More »</a>
</article>

<div class="abs footer-rule"></div>
<footer class="abs site-footer">
  <div class="abs footer-col" style="left:88px">
    <h4>CONTACT US</h4>
    <div class="contact-item"><svg width="18" height="14" viewBox="0 0 26 20" style="margin-top:4px"><rect x="1" y="1" width="24" height="18" fill="none" stroke="#fff" stroke-width="2"/><path d="M1 1l12 10L25 1" fill="none" stroke="#fff" stroke-width="2"/></svg><div><b>EMAIL ADDRESS</b><span>wendy.marsh.copywriter@mailbox-example.com</span></div></div>
    <div class="contact-item"><svg width="18" height="18" viewBox="0 0 24 24" style="margin-top:4px"><path d="M6.6 10.8a15 15 0 006.6 6.6l2.2-2.2a1 1 0 011-.25 11.4 11.4 0 003.6.6 1 1 0 011 1V20a1 1 0 01-1 1A17 17 0 013 4a1 1 0 011-1h3.5a1 1 0 011 1c0 1.25.2 2.45.57 3.57a1 1 0 01-.25 1z" fill="none" stroke="#fff" stroke-width="1.6"/></svg><div><b>PHONE NUMBER</b><span>0412 583 906</span></div></div>
  </div>
  <div class="abs footer-col" style="left:444px">
    <h4>ABOUT</h4>
    <ul><li>Home</li><li>About Us</li><li>Services</li><li>Portfolio</li></ul>
  </div>
  <div class="abs footer-col" style="left:657px">
    <h4>RESOURCES</h4>
    <ul><li>Blog</li><li>Copywriter</li><li>Faq</li><li>Contact</li></ul>
  </div>
  <div class="abs footer-col" style="left:876px">
    <h4>FOLLOW US OUT THERE</h4>
    <div class="socials"><span aria-label="Social link"></span><span aria-label="Social link"></span><span aria-label="Social link"></span><span aria-label="Social link"></span></div>
  </div>
</footer>
<div class="abs footer-bottom">© 2018 Company Name &nbsp;All right reserved</div>

</body>
</html>
```